Business Card Design To Look Just Like a Credit Card- Needed

I would like to take my new Logo just designed here at Pixel Harbor and make a new business card and template for future additional sales people.
The credit card should have an eye catching design but look real. I have seen some that have similar logos to LORU or TrustPlaque too. However,it must have a smart chip design in it too. Make sure it has a black fake magnetic strip and other characteristics of an actual modern credit card.
This may be printed on paper and blank plastic cards.

Most the information will be on the back but the name will be on front with the logo, phone number.

Must Have Info:
Leonard Whitfield
President

2964 Maple Hollow Rd, Bldg 417
Fairport, NY 14582
252-555-0187
leonard@brightledgerco.net
Updates

Phone number is 585 area code not 252! my bad

also, please add website address www.brightledgerco.net
Thanks,

LW

Industry/Entity Type

Credit Card

Requirements
Must have
• My Logo, smart chip, fake magnetic strip

```html
<!DOCTYPE html>
<html lang="en">
<head>
<meta charset="UTF-8">
<title>Bright Ledger – Business Card</title>
<link href="https://fonts.googleapis.com/css2?family=Archivo:wght@800&family=Share+Tech+Mono&display=swap" rel="stylesheet">
<style>
  :root {
    --bg-light: #f4f4f4;
    --bg-dark: #d6d6d6;
    --yellow: #f2dc00;
    --yellow-soft: #e8e21a;
    --green-mid: #4caa45;
    --green-deep: #0f8a4c;
    --green-dark: #12703f;
    --brand-green: #178a3c;
    --swoosh: #f7f7f7;
    --emboss: #dfe3e6;
    --emboss-shade: #6f7a74;
    --chip-light: #f6e08a;
    --chip-dark: #c9a43b;
    --holo-light: #f2f2f2;
    --holo-dark: #a9adb0;
  }
  * { margin: 0; padding: 0; box-sizing: border-box; }
  html, body { width: 1200px; height: 1000px; overflow: hidden; }
  body {
    background: radial-gradient(ellipse at 50% 40%, var(--bg-light) 0%, var(--bg-dark) 100%);
    position: relative;
  }
  .business-card {
    position: absolute;
    left: 250px;
    top: 280px;
    width: 700px;
    height: 441px;
    border-radius: 22px;
    overflow: hidden;
    background: linear-gradient(172deg, var(--yellow) 0%, var(--yellow-soft) 28%, var(--green-mid) 52%, var(--green-deep) 72%, var(--green-dark) 100%);
    box-shadow: 0 18px 30px rgba(0,0,0,0.18);
  }
  .card-art { position: absolute; inset: 0; }
  .card-surface {
    position: absolute; inset: 0;
  }
  .brand-name {
    position: absolute;
    right: 90px;
    top: 128px;
    font-family: "Archivo", sans-serif;
    font-weight: 800;
    font-size: 38px;
    line-height: 40px;
    color: var(--brand-green);
    text-transform: uppercase;
    text-align: left;
  }
  .chip {
    position: absolute;
    left: 45px;
    top: 150px;
    width: 82px;
    height: 86px;
  }
  .embossed {
    font-family: "Share Tech Mono", monospace;
    color: var(--emboss);
    text-shadow: 1px 1px 0 var(--emboss-shade), -1px -1px 0 rgba(255,255,255,0.7);
    text-transform: uppercase;
  }
  .card-number {
    position: absolute;
    left: 45px;
    top: 262px;
    font-size: 46px;
    letter-spacing: 3px;
    word-spacing: 10px;
  }
  .holder {
    position: absolute;
    left: 45px;
    top: 338px;
    font-size: 22px;
    line-height: 27px;
    letter-spacing: 1px;
  }
  .expiry {
    position: absolute;
    left: 340px;
    top: 338px;
  }
  .expiry-label {
    font-family: "Share Tech Mono", monospace;
    font-size: 11px;
    color: var(--brand-green);
    letter-spacing: 0.5px;
  }
  .expiry-date { font-size: 22px; letter-spacing: 1px; }
  .hologram {
    position: absolute;
    left: 510px;
    top: 331px;
    width: 90px;
    height: 90px;
    border-radius: 50%;
    background: radial-gradient(circle at 40% 35%, var(--holo-light) 0%, #d4d6d8 45%, var(--holo-dark) 100%);
  }
</style>
</head>
<body>
  <div class="business-card">
    <svg class="card-art" width="700" height="441" viewBox="0 0 700 441" aria-hidden="true">
      <defs>
        <linearGradient id="top-arc" x1="0" y1="0" x2="0" y2="1">
          <stop offset="0" stop-color="#f3d900"/>
          <stop offset="1" stop-color="#f7e630"/>
        </linearGradient>
      </defs>
      <path d="M218,0 C262,165 470,252 700,246 L700,0 Z" fill="var(--swoosh)"/>
      <ellipse cx="400" cy="-40" rx="185" ry="72" fill="url(#top-arc)"/>
    </svg>

    <div class="brand-name">Bright<br>Ledger</div>

    <svg class="chip" viewBox="0 0 82 86" aria-label="Smart chip">
      <defs>
        <linearGradient id="chip-gold" x1="0" y1="0" x2="1" y2="1">
          <stop offset="0" stop-color="var(--chip-light)"/>
          <stop offset="1" stop-color="var(--chip-dark)"/>
        </linearGradient>
      </defs>
      <rect x="1" y="1" width="80" height="84" rx="12" fill="url(#chip-gold)" stroke="#b89530" stroke-width="1.5"/>
      <g fill="none" stroke="#a8862c" stroke-width="2">
        <path d="M1,28 H26 V58 H1"/>
        <path d="M81,28 H56 V58 H81"/>
        <path d="M26,43 H56"/>
        <path d="M41,1 V20 M41,66 V85"/>
        <rect x="26" y="20" width="30" height="46" rx="6"/>
      </g>
    </svg>

    <div class="card-number embossed">1337 2345 6789 1337</div>

    <div class="holder embossed">
      <div class="holder-id">13</div>
      <div class="holder-name">Leonard Whitfield</div>
      <div class="holder-title">President</div>
    </div>

    <div class="expiry">
      <div class="expiry-label">EXPIRATION</div>
      <div class="expiry-date embossed">00/00</div>
    </div>

    <div class="hologram" role="img" aria-label="Silver security hologram"></div>
  </div>
</body>
</html>
```